Professional / Luxury Rack Card Design Needed (Do not use AI)

We are a private, boutique style optometry practice in College Station, Texas. We want the new design to communicate a premium, modern, luxury eye care experience while remaining professional and approachable.
When someone picks up this rack card, we want them to think:
"This practice looks modern, advanced, trustworthy, and premium. I would expect exceptional care and a high-end eyewear experience."

Target Market(s)

Families, professionals, adults seeking comprehensive medical eye care and vision correction. Patients seeking premium eyewear, advanced technology, and personalize care. Individuals and families seeking long term relationships with a trusted eye care provider. Patients who value exceptional service, expertise, and convenience.

Industry/Entity Type

Medical & Optometry-luxury optical

Font styles to use
Serif
Other font styles liked:
• Avenir if available. If not, Montserrat for headlines and Open Sans for Body text. For the slogan, use larger bold Montserrat.

Requirements
Must have
• Non-edited photo of doctors (merged together) with names. "Your Vision. Our Focus." Phone, website, Text/Call to Schedule appointment (Call to action to schedule). Accepting new patients. Eye Care center logo prominently displayed. Real photo of Eye Care Center building. Contact information (see attachement with all info)
Nice to have
• For frame brands, use the branded names. (see attachment)
Should not have
• Shouild not be busy/cluttered. Do not use scripted font from my website. Do NOT use AI generated images. Do not edit doctor faces other than merging them together. DO NOT use AI to edit faces....only to merge them side by side.

```html
<!DOCTYPE html>
<html lang="en">
<head>
<meta charset="utf-8">
<title>Brightview Clinic Rack Card</title>
<link href="https://fonts.googleapis.com/css2?family=Poppins:ital,wght@0,300;0,400;0,500;0,600;0,700;1,400;1,800&display=swap" rel="stylesheet">
<style>
  :root {
    --stage: #b6b7b9;
    --navy: #15202a;
    --navy-text: #2b3b4c;
    --slate: #3f4d5a;
    --gold: #dba227;
    --gold-band: #e7ad31;
    --paper: #f2f5f4;
    --sky: #c7d9e7;
    --aqua: #a8dde9;
    --steel: #3e5d74;
    --teal: #7fc4cf;
    --grey-text: #5b6168;
    --white: #ffffff;
  }
  * { box-sizing: border-box; margin: 0; padding: 0; }
  html, body { width: 1073px; height: 1200px; overflow: hidden; }
  body { background: var(--stage); font-family: "Poppins", sans-serif; position: relative; }

  .card { position: absolute; width: 430px; height: 966px; overflow: hidden; box-shadow: 0 3px 8px rgba(0,0,0,.25); }
  .card--front { left: 94px; top: 104px; background: var(--navy); }
  .card--back { left: 571px; top: 108px; background: var(--aqua); }

  /* front */
  .front-top { position: absolute; left: 0; top: 0; width: 430px; height: 130px; background: var(--paper); }
  .brand { position: absolute; left: 28px; top: 28px; width: 360px; height: 80px; }
  .brand__dot { position: absolute; left: 0; top: 4px; width: 58px; height: 58px; border-radius: 50%; background: var(--teal); }
  .brand__name { position: absolute; left: 84px; top: 0; font-size: 30px; font-weight: 400; color: var(--grey-text); letter-spacing: .5px; line-height: 44px; }
  .brand__rule { position: absolute; left: 84px; top: 43px; width: 270px; height: 1px; background: #b9bec2; }
  .brand__member { position: absolute; left: 84px; top: 50px; font-size: 8px; letter-spacing: 1.6px; color: var(--grey-text); line-height: 22px; }
  .brand__member b { font-size: 14px; font-weight: 400; letter-spacing: 1px; margin-left: 6px; }

  .hero { position: absolute; left: 0; top: 112px; width: 430px; height: 420px; }

  .slogan { position: absolute; left: 47px; top: 498px; font-size: 64px; line-height: 73px; font-weight: 700; color: var(--white); letter-spacing: -1px; }
  .slogan span { display: block; }
  .slogan .dot { color: var(--gold); display: inline; }
  .slogan .accent { color: var(--gold); font-style: italic; font-weight: 800; }

  .features { position: absolute; left: 22px; top: 800px; width: 390px; height: 70px; display: flex; }
  .feature { flex: 1; text-align: center; border-right: 1px solid #6d7884; font-size: 8.3px; line-height: 11px; color: var(--white); letter-spacing: .3px; }
  .feature:last-child { border-right: 0; color: var(--gold); }
  .feature svg { display: block; margin: 0 auto 6px; height: 26px; }

  .cta { position: absolute; left: 82px; top: 874px; width: 264px; height: 22px; background: var(--gold); color: var(--navy); font-size: 10.5px; font-weight: 600; letter-spacing: .9px; text-align: center; line-height: 22px; }
  .accepting { position: absolute; left: 0; top: 900px; width: 430px; text-align: center; font-size: 10.5px; font-style: italic; color: var(--white); letter-spacing: .4px; }

  .contact { position: absolute; left: 0; bottom: 0; width: 430px; height: 45px; background: var(--slate); color: var(--white); font-size: 6.4px; line-height: 9px; letter-spacing: .4px; }
  .contact__item { position: absolute; top: 13px; display: flex; align-items: center; gap: 6px; }
  .contact__item svg { width: 14px; height: 16px; flex: none; }
  .contact__site { color: var(--gold); }
  .contact__divider { position: absolute; top: 9px; width: 1px; height: 27px; background: #7b8791; }

  /* back */
  .back-top { position: absolute; left: 0; top: 0; width: 430px; height: 460px; background: linear-gradient(#c3d5e4, #cfdfe8); }
  .tagline { position: absolute; left: 0; top: 28px; width: 430px; text-align: center; font-size: 19px; font-weight: 700; letter-spacing: 2.6px; line-height: 25px; color: var(--navy-text); }
  .tagline__rule { position: absolute; top: 48px; width: 50px; height: 2px; background: #b8902c; }

  .doctor { position: absolute; top: 100px; width: 96px; text-align: center; }
  .doctor__photo { width: 89px; height: 89px; margin: 0 auto; border-radius: 50%; border: 2px solid var(--gold); background: radial-gradient(circle at 50% 70%, #f4f2ee 0 30%, #b39a7c 31% 100%); }
  .doctor__name { margin-top: 12px; font-size: 11px; font-weight: 600; color: var(--navy); white-space: nowrap; }

  .building { position: absolute; left: 0; top: 220px; width: 430px; height: 260px; }

  .section-title { position: absolute; display: flex; align-items: center; gap: 12px; font-size: 18px; font-weight: 600; color: var(--steel); letter-spacing: .2px; }
  .checks { position: absolute; list-style: none; font-size: 11.6px; line-height: 14px; color: var(--navy-text); }
  .checks li { position: absolute; left: 0; white-space: nowrap; padding-left: 18px; }
  .checks li svg { position: absolute; left: 0; top: 2px; width: 11px; height: 10px; }
  .services-band { position: absolute; left: 0; top: 726px; width: 430px; height: 200px; background: var(--gold-band); }
</style>
</head>
<body>

<!-- FRONT -->
<section class="card card--front">
  <div class="front-top">
    <div class="brand">
      <div class="brand__dot"></div>
      <div class="brand__name">brightviewclinic</div>
      <div class="brand__rule"></div>
      <div class="brand__member">A MEMBER OF <b>Optic Alliance</b></div>
    </div>
  </div>

  <svg class="hero" viewBox="0 0 430 420">
    <defs>
      <linearGradient id="heroFill" x1="0" y1="0" x2="1" y2="1">
        <stop offset="0" stop-color="#e7ecf0"/>
        <stop offset=".5" stop-color="#cfd9e2"/>
        <stop offset="1" stop-color="#7f9fc0"/>
      </linearGradient>
      <linearGradient id="navyFade" x1="0" y1="0" x2="0" y2="1">
        <stop offset="0" stop-color="#3b4650"/>
        <stop offset="1" stop-color="#15202a"/>
      </linearGradient>
    </defs>
    <rect x="0" y="230" width="430" height="190" fill="url(#navyFade)"/>
    <path d="M0 256 Q200 420 430 297 L430 280 Q210 380 0 250 Z" fill="#dba227"/>
    <path d="M0 0 H430 V291 Q215 382 0 250 Z" fill="url(#heroFill)" role="img" aria-label="Photo: optometrist fitting new glasses on a smiling male patient"/>
  </svg>

  <h1 class="slogan">
    <span>Your</span>
    <span>Vision<span class="dot">.</span></span>
    <span class="accent">Our</span>
    <span class="accent">Focus<span class="dot">.</span></span>
  </h1>

  <div class="features">
    <div class="feature">
      <svg viewBox="0 0 40 24" width="40"><path d="M2 12 Q20 -4 38 12 Q20 28 2 12 Z" fill="none" stroke="#fff" stroke-width="1.5"/><circle cx="20" cy="12" r="6" fill="none" stroke="#fff" stroke-width="1.5"/><circle cx="20" cy="12" r="3" fill="#7fc4cf"/></svg>
      COMPREHENSIVE<br>EYE CARE
    </div>
    <div class="feature">
      <svg viewBox="0 0 26 26" width="26"><circle cx="13" cy="13" r="11" fill="none" stroke="#fff" stroke-width="1.5"/><circle cx="13" cy="13" r="6" fill="none" stroke="#fff" stroke-width="1.5"/><circle cx="13" cy="13" r="3" fill="#dba227"/></svg>
      ADVANCED<br>TECHNOLOGY
    </div>
    <div class="feature">
      <svg viewBox="0 0 26 26" width="26"><circle cx="13" cy="8" r="6" fill="none" stroke="#dba227" stroke-width="1.5"/><path d="M2 25 Q2 15 13 15 Q24 15 24 25 Z" fill="none" stroke="#dba227" stroke-width="1.5"/></svg>
      PERSONALIZED<br>CARE
    </div>
    <div class="feature">
      <svg viewBox="0 0 42 20" width="42"><circle cx="10" cy="11" r="8" fill="none" stroke="#dba227" stroke-width="1.8"/><circle cx="32" cy="11" r="8" fill="none" stroke="#dba227" stroke-width="1.8"/><path d="M18 10 Q21 7 24 10" fill="none" stroke="#dba227" stroke-width="1.8"/></svg>
      OVER 1,000<br>DESIGNER FRAMES<br>&amp; SUNGLASSES
    </div>
  </div>

  <div class="cta">SCHEDULE YOUR APPOINTMENT TODAY</div>
  <p class="accepting">Accepting New Patients</p>

  <footer class="contact">
    <div class="contact__item" style="left:18px">
      <svg viewBox="0 0 14 16"><path d="M7 15 Q1 8 1 6 A6 6 0 0 1 13 6 Q13 8 7 15 Z" fill="none" stroke="#dba227" stroke-width="1.2"/><circle cx="7" cy="6" r="2" fill="none" stroke="#dba227" stroke-width="1.2"/></svg>
      <span>415 MEADOW PARK DR.<br>BRAZOS CITY, TX 77800</span>
    </div>
    <div class="contact__divider" style="left:150px"></div>
    <div class="contact__item" style="left:162px">
      <svg viewBox="0 0 14 16"><path d="M3 2 L6 5 L4.5 7 Q6 10 8.5 11.5 L10.5 10 L13 13 L11 15 Q4 13 1 5 Z" fill="none" stroke="#dba227" stroke-width="1.2"/></svg>
      <span>CALL OR TEXT<br>555.014.2020</span>
    </div>
    <div class="contact__divider" style="left:246px"></div>
    <div class="contact__item" style="left:262px">
      <svg viewBox="0 0 16 16"><circle cx="8" cy="8" r="7" fill="none" stroke="#dba227" stroke-width="1.2"/><ellipse cx="8" cy="8" rx="3" ry="7" fill="none" stroke="#dba227" stroke-width="1"/><path d="M1 8 H15 M2.5 4.5 H13.5 M2.5 11.5 H13.5" stroke="#dba227" stroke-width="1"/></svg>
      <span>MAKE YOUR APPOINTMENT ONLINE<br>WWW.<span class="contact__site">BRIGHTVIEWCLINIC.COM</span></span>
    </div>
  </footer>
</section>

<!-- BACK -->
<section class="card card--back">
  <div class="back-top"></div>
  <div class="tagline__rule" style="left:33px"></div>
  <div class="tagline__rule" style="left:348px"></div>
  <h2 class="tagline">EXPERT EYE CARE.<br>PERSONAL TOUCH.</h2>

  <div class="doctor" style="left:19px">
    <div class="doctor__photo" role="img" aria-label="Portrait of Dr. Ellison in a white coat"></div>
    <p class="doctor__name">Dr.Ellison, O.D</p>
  </div>
  <div class="doctor" style="left:121px">
    <div class="doctor__photo" role="img" aria-label="Portrait of Dr. Marsh in a white coat"></div>
    <p class="doctor__name">Dr.Marsh, O.D</p>
  </div>
  <div class="doctor" style="left:220px">
    <div class="doctor__photo" role="img" aria-label="Portrait of Dr. Navarro in a white coat"></div>
    <p class="doctor__name">Dr.Navarro, O.D</p>
  </div>
  <div class="doctor" style="left:319px">
    <div class="doctor__photo" role="img" aria-label="Portrait of Dr. Holt in a white coat"></div>
    <p class="doctor__name">Dr.Holt, O.D</p>
  </div>

  <svg class="building" viewBox="0 0 430 260">
    <defs>
      <linearGradient id="buildFill" x1="0" y1="0" x2="0" y2="1">
        <stop offset="0" stop-color="#cdd9e2"/>
        <stop offset=".3" stop-color="#e6ddbf"/>
        <stop offset=".7" stop-color="#9a8068"/>
        <stop offset="1" stop-color="#6e5a48"/>
      </linearGradient>
    </defs>
    <path d="M0 200 Q200 270 430 212 L430 225 Q200 285 0 210 Z" fill="#e7ad31"/>
    <path d="M0 110 Q210 30 430 60 L430 213 Q200 268 0 198 Z" fill="url(#buildFill)" role="img" aria-label="Photo: the clinic's stone and stucco building with arched windows"/>
  </svg>

  <div class="section-title" style="left:44px;top:502px">
    <svg viewBox="0 0 36 20" width="36" height="20"><path d="M1 10 Q18 -4 35 10 Q18 24 1 10 Z" fill="none" stroke="#3e5d74" stroke-width="1.3"/><circle cx="18" cy="10" r="5" fill="none" stroke="#3e5d74" stroke-width="1.3"/><circle cx="18" cy="10" r="2.5" fill="none" stroke="#3e5d74" stroke-width="1.1"/></svg>
    MEDICAL EYE CARE
  </div>

  <ul class="checks" style="left:48px;top:552px">
    <li style="top:0"><svg viewBox="0 0 11 10"><path d="M1 5 L4 8 L10 1" fill="none" stroke="#dba227" stroke-width="1.8"/></svg>Cataract</li>
    <li style="top:28px"><svg viewBox="0 0 11 10"><path d="M1 5 L4 8 L10 1" fill="none" stroke="#dba227" stroke-width="1.8"/></svg>Glaucoma</li>
    <li style="top:57px"><svg viewBox="0 0 11 10"><path d="M1 5 L4 8 L10 1" fill="none" stroke="#dba227" stroke-width="1.8"/></svg>Macular Defeneration</li>
    <li style="top:85px"><svg viewBox="0 0 11 10"><path d="M1 5 L4 8 L10 1" fill="none" stroke="#dba227" stroke-width="1.8"/></svg>Dry Eye &amp; Allergy</li>
    <li style="top:113px"><svg viewBox="0 0 11 10"><path d="M1 5 L4 8 L10 1" fill="none" stroke="#dba227" stroke-width="1.8"/></svg>Eye Injuries &amp; Infections</li>
  </ul>
  <ul class="checks" style="left:218px;top:553px">
    <li style="top:0"><svg viewBox="0 0 11 10"><path d="M1 5 L4 8 L10 1" fill="none" stroke="#dba227" stroke-width="1.8"/></svg>Ocular Disease<br>Management</li>
    <li style="top:42px"><svg viewBox="0 0 11 10"><path d="M1 5 L4 8 L10 1" fill="none" stroke="#dba227" stroke-width="1.8"/></svg>Surgery Co-Management</li>
    <li style="top:71px"><svg viewBox="0 0 11 10"><path d="M1 5 L4 8 L10 1" fill="none" stroke="#dba227" stroke-width="1.8"/></svg>Migraine &amp; Headache</li>
    <li style="top:99px"><svg viewBox="0 0 11 10"><path d="M1 5 L4 8 L10 1" fill="none" stroke="#dba227" stroke-width="1.8"/></svg>Eye Muscle Alignment</li>
  </ul>

  <div class="services-band"></div>
  <div class="section-title" style="left:38px;top:750px">
    <svg viewBox="0 0 42 20" width="42" height="20"><circle cx="10" cy="11" r="8" fill="none" stroke="#1c2733" stroke-width="1.6"/><circle cx="32" cy="11" r="8" fill="none" stroke="#1c2733" stroke-width="1.6"/><path d="M18 10 Q21 7 24 10" fill="none" stroke="#1c2733" stroke-width="1.6"/></svg>
    VISION SERVICES
  </div>

  <ul class="checks" style="left:46px;top:790px">
    <li style="top:0"><svg viewBox="0 0 11 10"><path d="M1 5 L4 8 L10 1" fill="none" stroke="#3e5d74" stroke-width="1.8"/></svg>Comprehensive<br>Eye Exams</li>
    <li style="top:41px"><svg viewBox="0 0 11 10"><path d="M1 5 L4 8 L10 1" fill="none" stroke="#3e5d74" stroke-width="1.8"/></svg>Pediatric Exams</li>
    <li style="top:69px"><svg viewBox="0 0 11 10"><path d="M1 5 L4 8 L10 1" fill="none" stroke="#3e5d74" stroke-width="1.8"/></svg>Specialty Contact<br>Lens Service</li>
  </ul>
  <ul class="checks" style="left:214px;top:789px">
    <li style="top:0"><svg viewBox="0 0 11 10"><path d="M1 5 L4 8 L10 1" fill="none" stroke="#3e5d74" stroke-width="1.8"/></svg>Advanced Diagnostic<br>Testing</li>
    <li style="top:41px"><svg viewBox="0 0 11 10"><path d="M1 5 L4 8 L10 1" fill="none" stroke="#3e5d74" stroke-width="1.8"/></svg>Surgery Co-Management</li>
    <li style="top:69px"><svg viewBox="0 0 11 10"><path d="M1 5 L4 8 L10 1" fill="none" stroke="#3e5d74" stroke-width="1.8"/></svg>Eye Muscle Alignment</li>
  </ul>

  <footer class="contact">
    <div class="contact__item" style="left:18px">
      <svg viewBox="0 0 14 16"><path d="M7 15 Q1 8 1 6 A6 6 0 0 1 13 6 Q13 8 7 15 Z" fill="none" stroke="#dba227" stroke-width="1.2"/><circle cx="7" cy="6" r="2" fill="none" stroke="#dba227" stroke-width="1.2"/></svg>
      <span>415 MEADOW PARK DR.<br>BRAZOS CITY, TX 77800</span>
    </div>
    <div class="contact__divider" style="left:150px"></div>
    <div class="contact__item" style="left:162px">
      <svg viewBox="0 0 14 16"><path d="M3 2 L6 5 L4.5 7 Q6 10 8.5 11.5 L10.5 10 L13 13 L11 15 Q4 13 1 5 Z" fill="none" stroke="#dba227" stroke-width="1.2"/></svg>
      <span>CALL OR TEXT<br>555.014.2020</span>
    </div>
    <div class="contact__divider" style="left:246px"></div>
    <div class="contact__item" style="left:262px">
      <svg viewBox="0 0 16 16"><circle cx="8" cy="8" r="7" fill="none" stroke="#dba227" stroke-width="1.2"/><ellipse cx="8" cy="8" rx="3" ry="7" fill="none" stroke="#dba227" stroke-width="1"/><path d="M1 8 H15 M2.5 4.5 H13.5 M2.5 11.5 H13.5" stroke="#dba227" stroke-width="1"/></svg>
      <span>MAKE YOUR APPOINTMENT ONLINE<br>WWW.<span class="contact__site">BRIGHTVIEWCLINIC.COM</span></span>
    </div>
  </footer>
</section>

</body>
</html>
```